Family Medicine Business Card Design Project

Looking for a very professional, clean, simple, minimalist, well designed business card.

I am reestablishing my medical practice in a new town and looking for a new look. I am currently in the process of revising my corporate identity. I recently changed the business name to Bright Path Family Medicine and had the logo redesigned.

You can visit the website http://brightpathfm.com/ to get a feel for what I may be looking for.

I am looking for a two sided business card.
I would like to include an appointment reminder on one side.
Colors would ideally be greens and blues, cool tones, or graytones.

I like the idea of including a QR code but only if able to do in a clean and simple design.

Things to include on business card
Dana Morrow, D.O.
Bright Path Family Medicine
4172 Lantern Row
Amarillo, TX 79382
Phone: 806-274-7284 (PATH)
Fax: 806-274-3817
Web: brightpathfm.com
facebook.com/BrightPathFamilyMedicine
Email:info@brightpathfm.com

Somehow list/bullets of, or specializing in:
Nutrition
Manipulation
Acupuncture
Prolotherapy
Functional Medicine

May include slogan
"Guiding you along a bright path"

I have attached the logo design, and other samples I have seen that have features that I may be looking for.

Reason: I apologize for extending the deadline, we are packing and moving tomorrow and I will not have internet for 3 day, I still need to give feedback and waiting on several revisions. I promise I will not extend deadline again.

Target Market(s)

Health conscious people of all ages looking for a family medicine doctor

Industry/Entity Type

Medical

Requirements
Must have
• I am looking for a two sided business card.
Nice to have
• Colors would ideally be greens and blues or graytones.

May include slogan

```html
<!DOCTYPE html>
<html lang="en">
<head>
<meta charset="utf-8">
<title>Bright Path Family Medicine – Appointment Reminder</title>
<link href="https://fonts.googleapis.com/css2?family=Tenor+Sans&display=swap" rel="stylesheet">
<style>
  :root {
    --card-center: #252525;
    --card-edge: #0e0e0e;
    --olive: #7a7431;
    --olive-line: #6f6a2c;
    --olive-soft: #6b6a2e;
  }
  html, body {
    margin: 0;
    padding: 0;
    width: 1200px;
    height: 741px;
    overflow: hidden;
    background: var(--card-edge);
  }
  .reminder-card {
    position: relative;
    width: 1200px;
    height: 741px;
    background: radial-gradient(ellipse at 45% 45%, var(--card-center) 0%, #1a1a1a 55%, var(--card-edge) 100%);
    font-family: "Tenor Sans", sans-serif;
    color: var(--olive);
    overflow: hidden;
  }
  .brand {
    position: absolute;
    left: 566px;
    top: 38px;
    display: flex;
    align-items: center;
    gap: 16px;
  }
  .brand-mark {
    width: 50px;
    height: 50px;
    border-radius: 50%;
    background: var(--olive-soft);
  }
  .brand-name {
    margin: 0;
    font-weight: 400;
    font-size: 42px;
    line-height: 1;
    color: var(--olive);
  }
  .brand-sub {
    display: block;
    margin-top: 10px;
    font-size: 16px;
    letter-spacing: 6px;
    color: var(--olive);
  }
  .clinic-address {
    position: absolute;
    left: 938px;
    top: 58px;
    margin: 0;
    font-style: normal;
    font-size: 20px;
    line-height: 27.5px;
    color: var(--olive-soft);
  }
  .card-title {
    position: absolute;
    left: 58px;
    top: 216px;
    margin: 0;
    font-weight: 400;
    font-size: 50px;
    line-height: 1;
    color: var(--olive);
  }
  .fill-field {
    position: absolute;
    left: 128px;
    width: 964px;
    border-bottom: 3px solid var(--olive-line);
    font-size: 44px;
    line-height: 1;
    height: 46px;
  }
  .field-for { top: 331px; }
  .field-date { top: 411px; }
  .field-blank { top: 490px; }
  .field-label { position: absolute; bottom: 0; }
  .label-time { left: 598px; }
  .reschedule-note {
    position: absolute;
    left: 0;
    right: 0;
    top: 700px;
    margin: 0;
    text-align: center;
    font-size: 25px;
    line-height: 1;
    color: var(--olive);
  }
</style>
</head>
<body>
  <main class="reminder-card">
    <div class="brand">
      <span class="brand-mark" aria-hidden="true"></span>
      <h1 class="brand-name">Bright Path<span class="brand-sub">FAMILY MEDICINE</span></h1>
    </div>
    <address class="clinic-address">
      Bright Path Family Medicine<br>
      4172 Lantern Row<br>
      Amarillo, TX 79382
    </address>

    <h2 class="card-title">Appointment Reminder</h2>

    <div class="fill-field field-for"><span class="field-label">For</span></div>
    <div class="fill-field field-date">
      <span class="field-label">Date</span>
      <span class="field-label label-time">Time</span>
    </div>
    <div class="fill-field field-blank"></div>

    <p class="reschedule-note">Please give us 24 hours notice if you need to reschedule your appointment</p>
  </main>
</body>
</html>
```